Emergency Vehicle Installer and Security Firm Needs a Business Card

Our company "Corvalt" need a business card for our Emergency Vehicle Equipment Installation and Infrastructure Security Business. We are contract designers, manufacturers and installers for Emergency Vehicle Fleets. This includes installation of Emergency Lights, Sirens, Vehicle Graphics and Radio Communications. We also supply this products to an international market. We also do consultant, and installation of high level security access, alarm and surveillance equipment for medium to large size businesses.

The design should represent a level of trust in our professionalism and expertise. It should visually display our ongoing relationship with the emergency services, but not overtake our commitment to high level security options.

Target Market(s)

Emergency Services and Businesses requiring high level security

Industry/Entity Type

Business

Contact Information for Business Card

*note complete details will be given to the winning designer for revising. The name "Mark Pell will be used to fill in name".

Mark Pell
Managing Director
Corvalt NZ Limited
Phone: +64 027 604 91352
Email: mark.pell@corvalt-example.co.nz

Requirements
Must have
• Card must be in black. Using our logo on the top as supplied. Designers should try having the reverse side as a blurred image of police lights (red and blue) with our logo in greyscale in the centre (this is not particularly a requirement, but feel free to play around with this option).
Nice to have
• A card design that looks good when spot UV printed. A clean compact and graphic design. A grey scale feel on the front (excluding logo, but you can play around with that idea). Rounded smooth text.
Should not have
• Will update this section as designs come through - feel free to submit what you feel would look good.

```html
<!DOCTYPE html>
<html lang="en">
<head>
<meta charset="utf-8">
<title>Corvalt NZ Limited – Business Card</title>
<link rel="stylesheet" href="https://fonts.googleapis.com/css2?family=Roboto:wght@400;700&family=Montserrat:wght@600;700&display=swap">
<style>
  :root {
    --page-bg: #ffffff;
    --card-black: #1f1a19;
    --text-white: #ffffff;
    --accent-red: #e0262b;
    --wordmark-grey: #c9c9cc;
    --light-blue: #1b3fb8;
    --light-red: #e3272c;
  }
  html, body {
    margin: 0;
    padding: 0;
    width: 1200px;
    height: 1200px;
    overflow: hidden;
    background: var(--page-bg);
    font-family: "Roboto", Arial, sans-serif;
  }
  .canvas {
    position: relative;
    width: 1200px;
    height: 1200px;
  }
  .card {
    position: absolute;
    left: 122px;
    width: 955px;
    height: 545px;
    border-radius: 40px;
    overflow: hidden;
  }
  .card-front {
    top: 35px;
    background: var(--card-black);
    color: var(--text-white);
  }
  .card-back {
    top: 619px;
  }

  .brand {
    position: absolute;
    right: 70px;
    top: 85px;
    text-align: right;
  }
  .brand-name {
    font-family: "Montserrat", Arial, sans-serif;
    font-weight: 700;
    font-size: 78px;
    line-height: 1;
    letter-spacing: 1px;
    text-transform: uppercase;
    color: var(--text-white);
  }
  .brand-legal {
    margin-top: 24px;
    font-family: "Montserrat", Arial, sans-serif;
    font-weight: 600;
    font-size: 25px;
    letter-spacing: 5px;
    text-transform: uppercase;
    color: var(--text-white);
  }

  .person {
    position: absolute;
    left: 72px;
    top: 318px;
  }
  .person-name {
    font-weight: 700;
    font-size: 38px;
    line-height: 1.1;
  }
  .person-role {
    margin-top: 6px;
    font-size: 28px;
    padding-left: 2px;
  }
  .contact-list {
    list-style: none;
    margin: 40px 0 0;
    padding: 0;
    font-size: 33px;
  }
  .contact-item {
    display: flex;
    align-items: center;
    gap: 20px;
    height: 48px;
  }
  .contact-icon {
    width: 30px;
    height: 30px;
    flex: none;
  }

  .back-art {
    position: absolute;
    inset: 0;
    background:
      radial-gradient(circle at 76% 46%, #ffffff 0%, #f3a9a0 5%, var(--light-red) 17%, rgba(200,30,40,0.85) 30%, rgba(120,20,60,0) 48%),
      radial-gradient(circle at 12% 48%, #e6f4ff 0%, #3a8cf0 6%, rgba(30,80,200,0) 20%),
      linear-gradient(100deg, #142a8a 0%, var(--light-blue) 35%, #3a2fa8 58%, #4a1f6a 75%, #151018 100%);
  }
  .back-brand {
    position: absolute;
    left: 0;
    right: 0;
    top: 238px;
    text-align: center;
  }
  .back-brand .brand-name {
    font-size: 96px;
    color: var(--wordmark-grey);
  }
  .back-brand .brand-legal {
    margin-top: 18px;
    font-size: 33px;
    letter-spacing: 6px;
    color: var(--wordmark-grey);
  }
</style>
</head>
<body>
<main class="canvas">
  <section class="card card-front" aria-label="Business card front">
    <div class="brand">
      <div class="brand-name">Corvalt</div>
      <div class="brand-legal">Corvalt NZ Limited</div>
    </div>

    <div class="person">
      <div class="person-name">Mark Pell</div>
      <div class="person-role">Managing Director</div>
      <ul class="contact-list">
        <li class="contact-item">
          <svg class="contact-icon" viewBox="0 0 30 30" aria-hidden="true">
            <rect x="8" y="2" width="14" height="26" rx="3" fill="none" stroke="var(--accent-red)" stroke-width="3"/>
            <circle cx="15" cy="23" r="1.8" fill="var(--accent-red)"/>
          </svg>
          <span>+64 027 604 91352</span>
        </li>
        <li class="contact-item">
          <svg class="contact-icon" viewBox="0 0 30 30" aria-hidden="true">
            <rect x="1" y="7" width="28" height="17" rx="1" fill="var(--accent-red)"/>
            <path d="M2 8 L15 18 L28 8 M2 23 L11 15 M28 23 L19 15" fill="none" stroke="var(--card-black)" stroke-width="1.8"/>
          </svg>
          <span>mark.pell@corvalt-example.co.nz</span>
        </li>
      </ul>
    </div>
  </section>

  <section class="card card-back" aria-label="Business card back">
    <div class="back-art" role="img" aria-label="Blurred photograph of red and blue emergency vehicle lights"></div>
    <div class="back-brand">
      <div class="brand-name">Corvalt</div>
      <div class="brand-legal">Corvalt NZ Limited</div>
    </div>
  </section>
</main>
</body>
</html>
```